Take out menu for The Lantern Nook Café

I'd like to have my menu re imagined.
Menu: (see LanternNookCafe Current menu file)
- Using the "new menu" and "cater menu" files which are updated over the LanternNookCafe Current menu
- Should be able to fit onto 11 x 17 parallel fold design
- Similar to current menu with headings and menu descriptions
- I do not have a font preference, whatever you think looks great and is easily readable
- More creative layout
- No pics of real foods
- Keeping the colors in "Salad, Grill, Sandwich, etc"
- The Cover page needs to be more of a cover, with all the same information, just more creative layout using the new logo attached.
- Do not need the "Harbor Pine Roasters" and "Belvanti" logos that are on the current menu..
- With the background colors I'd like to stay with either bright type of green to signify "fresh", bright yellow, sky blue and/or white.
- The ** menu items should be featured
- "LanternNookCafe Current Menu" cover has all the pertinent information that I would also like on the new menu. Front cover should include: Logo, address, phone, fax, email, hours, "Catering Trays Always Avaialable" "Visit thelanternnookcafe.com to see our weekly specials!" "Dine In, Take Out or Delivery" Facebook, Twitter, Instagram logos.
The above mentioned for the front cover do not need to be in that particular order.
- Prefer the logo to be over a white background always
- Back cover should have somewhere, maps shot (LNMap), "Free Parking" "Free Wireless" "Delivery Minimum $10"
- With the maps shot on back, please insert the logo where it currently says "The Lantern Nook Cafe"
The Lantern Nook Cafe is a breakfast and lunch cafe serving mostly corporate clientele. As the owner, I am laid back and whimsical and I'd like that to reflect in the designs. Nothing fancy or serious, that's not my intention with the design.
thelanternnookcafe.com
Any questions please ask. Thank you in advance to all the talented designers for working on my project, it is greatly appreciated!

```html
<!DOCTYPE html>
<html lang="en">
<head>
<meta charset="utf-8">
<title>The Lantern Nook Café — Menu Inside Spread</title>
<link href="https://fonts.googleapis.com/css2?family=Fredoka:wght@600&family=PT+Sans+Narrow:wght@400;700&display=swap" rel="stylesheet">
<style>
:root{
  --garden:#1f9a4a; --garden-text:#2a8a3c; --garden-bg1:#fdf6c0; --garden-bg2:#fbeea0;
  --grill:#b3202b; --grill-text:#c0272f; --grill-bg1:#f4f6d2; --grill-bg2:#dcecb6;
  --sand:#1f3f8a; --sand-text:#1f3f8f; --sand-bg1:#cfeaf8; --sand-bg2:#eef8fd;
  --soup:#8b5aa8; --brk:#f06a22; --brk-text:#e8561a; --brk-bg1:#fdf3a8; --brk-bg2:#fde38a;
  --combo:#e8892a; --red:#d8202a; --ink:#111;
}
*{box-sizing:border-box;margin:0;padding:0}
html,body{width:1200px;height:780px;overflow:hidden;background:#fff}
body{font-family:"PT Sans Narrow",sans-serif;color:var(--ink);font-size:9.6px;line-height:1.2}
.spread{display:flex;width:1200px;height:780px}
.panel{position:relative;width:300px;height:780px;padding:30px 26px 26px 28px;display:flex;flex-direction:column}
.panel-bg{position:absolute;inset:0;z-index:0}
.panel>*:not(.panel-bg){position:relative;z-index:1}
.garden .panel-bg{background:linear-gradient(160deg,var(--garden-bg1),var(--garden-bg2))}
.grill .panel-bg{background:linear-gradient(180deg,var(--grill-bg1),var(--grill-bg2))}
.sandwiches .panel-bg{background:linear-gradient(180deg,var(--sand-bg1),var(--sand-bg2) 60%,var(--sand-bg1))}
.breakfast-col .panel-bg{background:linear-gradient(170deg,var(--brk-bg1),var(--brk-bg2))}
.pill{align-self:center;width:150px;height:30px;border-radius:50%;color:#fff;font-family:"Fredoka",sans-serif;font-weight:600;font-size:17px;letter-spacing:.5px;display:flex;align-items:center;justify-content:center;margin-bottom:18px;flex:none}
.pill.garden-h{background:var(--garden)} .pill.grill-h{background:var(--grill)}
.pill.sand-h{background:var(--sand);width:170px} .pill.soup-h{background:var(--soup)}
.pill.brk-h{background:var(--brk);width:160px} .pill.combo-h{background:var(--combo);margin:16px 0 10px}
.intro{font-weight:700;margin-bottom:8px}
.items{flex:1;display:flex;flex-direction:column;justify-content:space-between}
.item-name{font-weight:700;font-size:11.4px;margin-bottom:2px}
.item-name .price{color:var(--ink)}
.garden .item-name{color:var(--garden-text)} .grill .item-name{color:var(--grill-text)}
.sandwiches .item-name{color:var(--sand-text)} .breakfast .item-name{color:var(--brk-text)}
.featured{color:var(--red)}
.addon{font-weight:700;font-size:9px}
.grill .addon{color:var(--grill-text)} .sandwiches .addon{color:var(--sand-text)}
.dressings b{color:var(--garden-text)}
.dressings{font-weight:700}
.soup-prices{display:flex;justify-content:center;gap:50px;font-weight:700;font-size:10px}
.soup-note{text-align:center;font-weight:700;font-size:10px;margin-bottom:6px}
.combo{text-align:center;font-weight:700;font-size:11px}
.combo-grid{display:grid;grid-template-columns:1fr 1fr;width:140px;margin:6px auto 0;font-weight:700;font-size:9.6px}
.pair{display:flex;justify-content:space-between}
.pair .item-name{display:inline}
.bullet{text-align:center;padding-left:14px}
.notice{text-align:center;color:var(--red);font-weight:700;font-size:11px;line-height:1.25;margin-top:8px}
</style>
</head>
<body>
<main class="spread">

<section class="panel garden">
  <div class="panel-bg" role="img" aria-label="Soft yellow background with a faint pattern of purple leaves"></div>
  <h2 class="pill garden-h">GARDEN</h2>
  <p class="intro">Choose either on a bed of greens with homemade croutons or in a wheat, white or spinach wrap, served cold</p>
  <div class="items">
    <p class="item-name">Salad: <span class="price">Lg. — 6.75 &nbsp;&nbsp; Wrap: — 6.25 &nbsp;&nbsp; SM. — 4.50</span></p>
    <div><p class="item-name">** Apple Walnut</p><p>Romaine lettuce, diced chicken, tomatoes, craisins, diced apple, crumbled bleu cheese, walnuts and ranch dressing</p></div>
    <div><p class="item-name">Caesar</p><p>Romaine lettuce, diced chicken, sliced egg, parmesan cheese and creamy caesar dressing</p></div>
    <div><p class="item-name">Turkey</p><p>Romaine lettuce, home cooked all natural turkey, bacon, tomatoes, mixed cheese and French dressing</p></div>
    <div><p class="item-name">Cali Cobb</p><p>Romaine lettuce, diced chicken, avocado, tomatoes, bacon, egg, bleu cheese crumbles and avocado ranch dressing</p></div>
    <div><p class="item-name">Greek</p><p>Spinach, diced chicken, black olives, tomatoes, red onions, cucumber, feta cheese and balsamic vinaigrette dressing</p></div>
    <div><p class="item-name">Asian Sesame</p><p>Romaine lettuce, diced chicken, mandarin oranges, sliced almonds, carrots, sesame seeds and Asian sesame dressing</p></div>
    <div><p class="item-name">Chef’s</p><p>Romaine lettuce, home cooked all natural turkey, tavern ham, Swiss cheese, egg, bacon, tomatoes, red onions, cucumbers and Thousand Island dressing</p></div>
    <div><p class="item-name">Tomato, Mozzarella &amp; Spinach</p><p>Spinach, tomatoes, cucumbers, sautéed onions, fresh mozzarella and olive oil vinaigrette dressing</p></div>
    <div><p class="item-name">Tuna Salad Salad</p><p>Romaine lettuce, homemade all white tuna salad, Swiss cheese, tomatoes, carrots, red onions and balsamic vinaigrette dressing</p></div>
    <div><p class="item-name">House Garden Salad: <span class="price">Lg. — 5.25 &nbsp;Sm. — 1.95 &nbsp;Wrap — 5.50</span></p><p>Romaine lettuce, tomatoes, cucumber, carrots, red onions, shredded cheese blend and choice of dressing</p></div>
    <p class="dressings"><b>Dressings:</b> Asian Sesame, Avocado Ranch, Balsamic Vinaigrette, Bleu Cheese, Creamy Caesar, Creamy Italian, Fat Free Raspberry Vinaigrette, French, Honey Mustard, Olive Oil Vinaigrette, Ranch, Thousand Island</p>
  </div>
</section>

<section class="panel grill">
  <div class="panel-bg" role="img" aria-label="Pale green background with a faint pattern of pink flames"></div>
  <h2 class="pill grill-h">GRILL</h2>
  <div class="items">
    <div><p class="item-name"><span class="featured">**</span>Commerce Pita <span class="price">— 6.25</span></p><p>Grilled chicken, provolone, spinach, bacon and ranch on pita bread. Kick it up and ask for cajun seasoning!</p></div>
    <div><p class="item-name">Philly Cheesesteak <span class="price">— 5.95</span></p><p>Beef or chicken with choice of cheese. Toppings — 25 each</p></div>
    <div><p class="item-name">Burger/Veggie Burger <span class="price">— 5.95</span></p><p>Beef or veggie on a kaiser roll with choice of cheese, lettuce, tomato and red onion</p></div>
    <div><p class="item-name">Barbecue Chicken Panini <span class="price">— 6.25</span></p><p>Grilled chicken, BBQ sauce, red onions, bacon, cheddar cheese and ranch on sourdough</p></div>
    <div><p class="item-name">Fajita Wrap <span class="price">— 6.25</span></p><p>Seasoned chicken, peppers, onions and mixed cheese in a wrap, served with sour cream and salsa</p></div>
    <div><p class="item-name">Reuben / Rachel <span class="price">— 6.25</span></p><p>Choose from home cooked all natural turkey, home cooked roast beef or tavern ham, with kraut or coleslaw, Swiss and Thousand Island on marble rye</p></div>
    <div><p class="item-name">Veggie Panini <span class="price">— 6.25</span></p><p>Fresh mozzarella cheese, spinach, tomato, cucumber, red onions, roasted red peppers and balsamic vinaigrette on whole grain bread</p></div>
    <div><p class="item-name">Cajun Chicken Sandwich <span class="price">— 6.25</span></p><p>Grilled chicken with cajun seasoning, provolone or pepper jack cheese, onions, tomato and ranch on a kaiser roll</p></div>
    <div><p class="item-name">Chicken Mozz Panini <span class="price">— 6.50</span></p><p>Grilled chicken, tomatoes, spinach balsamic vinaigrette and fresh mozzarella on sourdough</p></div>
    <div><p class="item-name">California Club Sandwich <span class="price">— 6.50</span></p><p>Grilled chicken, fresh avocado, bacon, Swiss, lettuce, tomato and honey mustard on a kaiser roll</p></div>
    <div><p class="item-name">Chipotle Ranch Turkey Pita <span class="price">— 6.50</span></p><p>Home cooked all natural turkey, bacon, red onion, pepper-jack cheese and chipotle ranch on pita bread</p></div>
    <div><p class="item-name">Hot Roast Beef <span class="price">— 6.50</span></p><p>Home cooked roast beef in au jus, sautéed onions, horseradish sauce and provolone cheese baked on a hoagie roll</p></div>
    <div><p class="item-name">Tuna Melt <span class="price">— 6.50</span></p><p>Homemade all white tuna salad, tomatoes, and Swiss baked on sourdough</p></div>
    <div><p class="item-name">Mediterranean Panini <span class="price">— 6.50</span></p><p>Grilled chicken, fresh mozzarella, roasted red peppers and spinach on sourdough</p></div>
    <div><p class="item-name">Crazy Cheese <span class="price">— 4.25</span></p><p>Cheddar, American, Swiss, and tomato on sourdough. Add bacon 1.50</p></div>
    <p class="addon">Add chips and a pickle — 00.50</p>
  </div>
</section>

<section class="panel sandwiches">
  <div class="panel-bg" role="img" aria-label="Sky blue background with a faint pattern of white sandwich shapes"></div>
  <h2 class="pill sand-h">SANDWICHES</h2>
  <p class="intro">On choice of bread or wrap</p>
  <div class="items">
    <div><p class="item-name"><span class="featured">**</span> Turkey Club <span class="price">— 6.50</span></p><p>A triple decker! Home cooked all natural turkey, tomato, bacon, lettuce, Swiss and mayo. Add sun-dried tomato pesto — 00.25</p></div>
    <div><p class="item-name">B.L.T. <span class="price">— 5.25</span></p><p>A true classic with bacon, iceberg lettuce, tomato and mayo</p></div>
    <div><p class="item-name">Junkyard <span class="price">— 6.50</span></p><p>Home cooked roast beef, home cooked all natural turkey, tavern ham, pepperoni, lettuce, tomato, Swiss and mayo</p></div>
    <div><p class="item-name">Cold Roast Beef <span class="price">— 6.50</span></p><p>Home cooked roast beef, lettuce, tomato, Swiss and spicy horseradish sauce</p></div>
    <div><p class="item-name">Tuna Salad <span class="price">— 6.50</span></p><p>Homemade all white tuna, with lettuce and tomato. Add cheese .25</p></div>
    <div><p class="item-name">Veggie Avocado <span class="price">— 6.50</span></p><p>Avocado, roasted peppers, cucumber, red onions, feta cheese, lettuce, tomato and balsamic vinaigrette</p></div>
    <div><p class="item-name">Turkey Bacon Ranch <span class="price">— 6.50</span></p><p>Home cooked all natural turkey, bacon, cheddar cheese, lettuce, tomato and ranch</p></div>
    <div><p class="item-name">Italian <span class="price">— 6.50</span></p><p>Cappicola, salami, pepperoni, provolone, lettuce, tomato and onion</p></div>
    <div><p class="item-name">Ham and Swiss <span class="price">— 6.25</span></p><p>Sliced tavern ham and Swiss with lettuce, tomato, mayo and mustard</p></div>
    <div><p class="item-name">Chicken Salad <span class="price">— 6.25</span></p><p>Made to order with lettuce and tomato. Add cheese — 00.25</p></div>
    <div><p class="item-name">Egg Salad <span class="price">— 5.95</span></p><p>Made to order with lettuce and tomato. Add cheese — 00.25</p></div>
    <div><p class="item-name">PBB&amp;J <span class="price">— 4.95</span></p><p>Peanut butter or Hazelnutta and jelly with bananas, lightly grilled</p></div>
    <p class="addon">Add chips and a pickle — 00.50</p>
  </div>
  <h2 class="pill combo-h">COMBOS</h2>
  <p class="combo">Choose two — 6.50</p>
  <div class="combo-grid"><span>½ Sandwich<br>Soup</span><span>½ Salad<br>Quiche</span></div>
  <div style="height:34px"></div>
</section>

<section class="panel breakfast-col">
  <div class="panel-bg" role="img" aria-label="Bright yellow background with a faint pattern of orange suns"></div>
  <h2 class="pill soup-h">SOUP</h2>
  <div class="soup-prices"><span>8 oz — 3.15</span><span>12 oz — 3.50</span></div>
  <p class="soup-note">*Some soups — 00.50 extra*</p>
  <h2 class="pill brk-h" style="margin-bottom:14px">BREAKFAST</h2>
  <div class="items breakfast">
    <div><p class="item-name"><span class="featured">**</span>Cheesesteak Breakfast Wrap <span class="price">— 4.50</span></p><p>Two eggs, chopped steak, onions and American cheese in a wrap</p></div>
    <div><p class="item-name">Breakfast Sandwich <span class="price">— 3.50</span></p><p>Two eggs and American cheese on toast or English muffin with choice of meat</p><p class="bullet">• On a bagel add — 00.50 &nbsp; • On a croissant add — 1.00</p></div>
    <div><p class="item-name">Eggs Your Way <span class="price">— 3.75</span></p><p>Two eggs cooked to order with meat and toast</p></div>
    <div><p class="item-name">Omelet <span class="price">— 4.50</span></p><p>2 eggs with your choice of up to 3 fillings and toast</p></div>
    <div><p class="item-name">Burrito <span class="price">— 4.50</span></p><p>Two eggs, meat, mixed cheese, onions, peppers and salsa in a wrap</p></div>
    <div><p class="item-name">Greek Pita <span class="price">— 4.50</span></p><p>Two eggs, spinach and feta on a pita</p></div>
    <div><p class="item-name">Avocado Egg Croissant <span class="price">— 4.50</span></p><p>Two eggs, avocado and cheddar cheese on a croissant</p></div>
    <div><p class="item-name">B.E.L.T <span class="price">— 4.50</span></p><p>Egg, bacon, lettuce and tomato on choice of toast or English muffin. Add cheese — 00.25</p></div>
    <div><p class="item-name">French Toast <span class="price">— 4.50</span></p><p>Two thick slices of brioche with choice of meat</p></div>
    <div><p class="item-name">Pancakes <span class="price">— 4.25</span></p><p>Three pancakes with choice of meat</p></div>
    <div><p class="pair" style="width:190px"><span class="item-name">Quiche <span class="price">— 3.75</span></span><span class="item-name">Bagel <span class="price">— 2.15</span></span></p><p>Toasted with cream cheese, butter or jelly</p></div>
    <p class="pair" style="width:190px"><span class="item-name">Croissant <span class="price">— 1.95</span></span><span class="item-name">Muffin <span class="price">— 1.95</span></span></p>
    <p class="pair" style="width:222px"><span class="item-name">English Muffin <span class="price">— 1.55</span></span><span class="item-name">Side of hash browns <span class="price">— 1.50</span></span></p>
    <div><p class="item-name">Side of meat <span class="price">— 1.50</span></p><p class="bullet">• &nbsp;bacon, sausage, ham, turkey sausage or pork roll</p></div>
    <p class="item-name">Toast <span class="price">— 1.25</span></p>
  </div>
  <p class="notice">Menu items and prices subject to change<br>If you don’t see what you want on the menu, we will try and make it for you!</p>
</section>

</main>
</body>
</html>
```